Communication Skill: NODE Assist

I need a Design for a skill I teach to youth. That's why the title NODE Assist. NODE stands for Thoughts, Emotions, Concerns, Hopes & Desires. Under each word are some examples that are meant to help people discuss certain things. I tried to create something myself but want something much more creative and dynamic. I have attached what I designed because it has the information I need in the design. Want it to have a techie look to it.

```html
<!DOCTYPE html>
<html lang="en">
<head>
<meta charset="utf-8">
<title>NODE Assist</title>
<link rel="stylesheet" href="https://fonts.googleapis.com/css2?family=League+Spartan:wght@700;800&family=Fredoka:wght@600&family=Arimo:wght@400&display=swap">
<style>
  :root {
    --page: #c6c9d6;
    --thoughts: #e0354f;
    --emotions: #355add;
    --concerns: #3a8be0;
    --hopes: #c32bc6;
    --ink: #e9e1d6;
    --line: #ffffff;
  }
  * { box-sizing: border-box; margin: 0; padding: 0; }
  html, body { width: 1200px; height: 1200px; overflow: hidden; }
  body { background: var(--page); position: relative; }

  .poster {
    position: absolute; left: 40px; top: 204px;
    width: 1120px; height: 792px;
    display: flex; overflow: hidden;
  }
  .pillar { position: relative; width: 280px; height: 100%; }
  .pillar--thoughts { background: var(--thoughts); }
  .pillar--emotions { background: var(--emotions); }
  .pillar--concerns { background: var(--concerns); }
  .pillar--hopes { background: var(--hopes); }

  .pillar__icon {
    position: absolute; left: 50%; top: 44px; width: 72px; height: 72px;
    margin-left: -36px; border-radius: 50%;
    background: radial-gradient(circle, rgba(233,225,214,.55), rgba(233,225,214,.15));
  }
  .pillar__letter {
    position: absolute; left: 0; right: 0; top: 150px;
    text-align: center; color: var(--ink);
    font-family: "League Spartan", sans-serif; font-weight: 800;
    font-size: 262px; line-height: 1;
  }
  .pillar__word {
    position: absolute; left: 0; right: 0; top: 369px;
    text-align: center; color: var(--ink);
    font-family: "Fredoka", sans-serif; font-weight: 600;
    font-size: 30px; letter-spacing: 1px; line-height: 1;
  }

  .bubble {
    position: absolute; top: 675px; left: 19px; width: 232px; height: 85px;
    border: 2px solid var(--line); border-radius: 18px;
    padding: 8px 0 0 24px;
    color: var(--line); font-family: "Arimo", sans-serif;
    font-size: 13.5px; line-height: 17.5px;
  }
  .pillar--emotions .bubble, .pillar--hopes .bubble { left: 29px; padding-left: 27px; }
  .bubble__tail { position: absolute; bottom: -18px; width: 26px; height: 20px; }
  .bubble--tail-right .bubble__tail { right: -12px; }
  .bubble--tail-left .bubble__tail { left: -12px; }

  .signal-wave {
    position: absolute; left: 0; top: 480px; width: 1120px; height: 320px;
    background: linear-gradient(170deg, transparent 30%, rgba(90,190,255,.18) 55%, transparent 75%);
    pointer-events: none;
  }

  .title-box {
    position: absolute; left: 321px; top: 432px; width: 463px; height: 81px;
    border: 2px solid var(--line);
    display: flex; align-items: center; justify-content: center;
    color: var(--ink); font-family: "Fredoka", sans-serif; font-weight: 600;
    font-size: 60px; letter-spacing: 3px; line-height: 1; padding-top: 4px;
  }
</style>
</head>
<body>
  <main class="poster">
    <section class="pillar pillar--thoughts">
      <div class="pillar__icon" role="img" aria-label="Brain icon"></div>
      <div class="pillar__letter">N</div>
      <h2 class="pillar__word">THOUGHTS</h2>
      <div class="bubble bubble--tail-right">
        <p>“ It seems...”</p>
        <p>“ I wonder...”</p>
        <p>“ I believe...”</p>
        <p>“ It’s my opinion...”</p>
        <svg class="bubble__tail" viewBox="0 0 26 20"><path d="M0 0 L26 20 L14 0" fill="none" stroke="#fff" stroke-width="2"/><path d="M1 0 L24 18 L12 0Z" fill="var(--thoughts)"/></svg>
      </div>
    </section>
    <section class="pillar pillar--emotions">
      <div class="pillar__icon" role="img" aria-label="Heart with pulse line icon"></div>
      <div class="pillar__letter">O</div>
      <h2 class="pillar__word">EMOTIONS</h2>
      <div class="bubble bubble--tail-left">
        <p>I’m...</p>
        <p>hopeful - worried - sad</p>
        <p>affraid - mad - glad - happy</p>
        <p>confident - insecure...</p>
        <svg class="bubble__tail" viewBox="0 0 26 20"><path d="M26 0 L0 20 L12 0" fill="none" stroke="#fff" stroke-width="2"/><path d="M25 0 L2 18 L14 0Z" fill="var(--emotions)"/></svg>
      </div>
    </section>
    <section class="pillar pillar--concerns">
      <div class="pillar__icon" role="img" aria-label="Head silhouette with lightning icon"></div>
      <div class="pillar__letter">D</div>
      <h2 class="pillar__word">CONCERNS</h2>
      <div class="bubble bubble--tail-right">
        <p>“ I’m worry about...”</p>
        <p>“ I’m afraid that...”</p>
        <p>“ I’m nervous because...”</p>
        <p>“ It bothers me that...”</p>
        <svg class="bubble__tail" viewBox="0 0 26 20"><path d="M0 0 L26 20 L14 0" fill="none" stroke="#fff" stroke-width="2"/><path d="M1 0 L24 18 L12 0Z" fill="var(--concerns)"/></svg>
      </div>
    </section>
    <section class="pillar pillar--hopes">
      <div class="pillar__icon" role="img" aria-label="Dove icon"></div>
      <div class="pillar__letter">E</div>
      <h2 class="pillar__word">HOPES</h2>
      <div class="bubble bubble--tail-left">
        <p>I hope...</p>
        <p>I wish...</p>
        <p>It’s my desire...</p>
        <p>I’d like to see...</p>
        <svg class="bubble__tail" viewBox="0 0 26 20"><path d="M26 0 L0 20 L12 0" fill="none" stroke="#fff" stroke-width="2"/><path d="M25 0 L2 18 L14 0Z" fill="var(--hopes)"/></svg>
      </div>
    </section>

    <div class="signal-wave" role="img" aria-label="Flowing line wave pattern across the pillars"></div>
    <h1 class="title-box">ASSIST</h1>
  </main>
</body>
</html>
```